Lanternfield Route Courier Postcard Design Project-Feb 2018

See attached Center Profile. We need a postcard with one side describing the co-working center and the other side, the upcoming events.

Events

```html
<!DOCTYPE html>
<html lang="en">
<head>
<meta charset="utf-8">
<title>The Keystone Commons – Postcard</title>
<link rel="stylesheet" href="https://fonts.googleapis.com/css2?family=Exo+2:wght@700;800&family=Varela+Round&family=Oswald:wght@400;500&display=swap">
<style>
:root{
  --page:#ebe6de;
  --card:#ffffff;
  --orange:#f0822a;
  --slate:#646464;
  --ink:#2f2f2f;
  --sky:#7fcde0;
}
*{box-sizing:border-box;margin:0;padding:0}
html,body{width:1200px;height:1200px;overflow:hidden;background:var(--page)}
body{position:relative;font-family:"Varela Round",sans-serif;color:var(--ink)}
.card{position:absolute;left:246px;width:708px;height:517px;background:var(--card);overflow:hidden;box-shadow:0 4px 14px rgba(0,0,0,.25)}
.card--front{top:73px}
.card--back{top:611px}
.abs{position:absolute}
.art{position:absolute;left:0;top:0}
.brand{position:absolute;display:flex;align-items:center;gap:10px;font-family:"Varela Round",sans-serif;color:#333;white-space:nowrap;line-height:1}
.brand__dot{width:34px;height:34px;border-radius:50%;background:var(--orange);flex:none}
.headline{right:30px;text-align:right;font-family:"Exo 2",sans-serif;font-weight:800;color:var(--orange);line-height:1;white-space:nowrap}
.band-title{right:30px;top:232px;font-family:"Exo 2",sans-serif;font-weight:700;font-size:15px;color:var(--orange);white-space:nowrap}
.dots{position:absolute;border-top:2px dotted #e8e8e8;height:0}
.features{right:30px;top:266px;list-style:none;text-align:right;color:#fff;font-size:12px;line-height:19.5px;white-space:nowrap}
.features li::after{content:"";display:inline-block;width:5px;height:5px;border-radius:50%;background:var(--orange);margin-left:10px;vertical-align:2px}
.pitch{right:30px;top:376px;text-align:right;font-size:9.6px;line-height:13px;color:#333;white-space:nowrap}
.pitch em{font-style:normal;color:var(--orange)}
.contact-line{right:30px;display:flex;align-items:center;gap:9px;white-space:nowrap}
.web{font-size:15px;color:#333}
.web b{color:var(--orange);font-family:"Exo 2",sans-serif;font-weight:700}
.addr{font-family:"Oswald",sans-serif;font-weight:500;font-size:11px;color:#333}
.icon{width:18px;height:18px;flex:none}
/* back */
.inst-title{left:21px;top:135px;font-family:"Exo 2",sans-serif;font-weight:800;font-size:14px;color:var(--orange);white-space:nowrap}
.inst-copy{left:21px;top:163px;width:193px;font-size:9.4px;line-height:11.6px;color:#fff;text-align:justify}
.events-title{left:20px;top:219px;font-family:"Exo 2",sans-serif;font-weight:700;font-size:13.5px;color:#fff;white-space:nowrap}
.event{position:absolute;font-family:"Oswald",sans-serif;color:#fff;line-height:1.2;white-space:nowrap}
.event__name{font-family:"Exo 2",sans-serif;font-weight:700;font-size:10px;color:var(--orange)}
.event__host{font-size:7.5px;color:var(--orange)}
.event__when{font-size:7.5px;margin-top:3px}
.back-contact{left:20px;display:flex;align-items:center;gap:9px;color:#fff;white-space:nowrap}
.back-contact .icon{width:17px;height:17px}
.postage{left:552px;top:32px;width:123px;height:95px;border:1px solid #444;font-family:Arial,sans-serif;font-size:11.5px;line-height:14.5px;text-align:center;padding-top:11px;color:#222}
.mailbox{left:483px;top:377px;width:192px;height:76px;border:1px solid #444;font-family:Arial,sans-serif;color:#222}
.mailbox__route{position:absolute;right:14px;top:8px;font-size:8.5px}
.mailbox__to{position:absolute;left:14px;top:37px;font-size:11.5px;line-height:13px}
</style>
</head>
<body>

<!-- FRONT: co-working space -->
<section class="card card--front" aria-label="Postcard front">
  <svg class="art" width="708" height="517" viewBox="0 0 708 517">
    <defs>
      <linearGradient id="interior" x1="0" y1="0" x2="1" y2="1">
        <stop offset="0" stop-color="#6d4a36"/>
        <stop offset=".5" stop-color="#9c7a60"/>
        <stop offset="1" stop-color="#cfcac4"/>
      </linearGradient>
      <linearGradient id="balcony" x1="0" y1="0" x2="0" y2="1">
        <stop offset="0" stop-color="#c9d2d9"/>
        <stop offset=".55" stop-color="#aab3b8"/>
        <stop offset="1" stop-color="#6e5a4c"/>
      </linearGradient>
      <linearGradient id="haze" x1="0" y1="0" x2="1" y2="0">
        <stop offset="0" stop-color="#ffffff"/>
        <stop offset="1" stop-color="#eceef0"/>
      </linearGradient>
    </defs>
    <rect x="282" y="0" width="426" height="202" fill="url(#haze)"/>
    <rect x="282" y="202" width="426" height="159" fill="var(--slate)"/>
    <rect x="282" y="361" width="426" height="156" fill="#f1f1f1"/>
    <path role="img" aria-label="Photo of the open lounge inside the shared workspace" d="M0,170 C120,150 260,168 330,238 C378,288 400,340 396,420 L396,517 L0,517 Z" fill="url(#interior)"/>
    <path d="M0,150 C160,120 320,170 390,290 C420,350 420,440 400,517" fill="none" stroke="var(--sky)" stroke-width="1"/>
    <circle role="img" aria-label="Photo of people talking on the riverfront balcony" cx="170" cy="127" r="114" fill="url(#balcony)"/>
    <circle cx="170" cy="127" r="116" fill="none" stroke="var(--orange)" stroke-width="1.2"/>
  </svg>

  <div class="brand" style="right:30px;top:30px;font-size:28px">
    <span class="brand__dot"></span>the keystone commons
  </div>

  <div class="abs headline" style="top:96px;font-size:27px">YOUR MINDFUL,</div>
  <div class="abs headline" style="top:130px;font-size:32.5px">SHARED WORKSPACE</div>
  <div class="abs headline" style="top:168px;font-size:21px">ON THE WATERFRONT</div>

  <div class="abs band-title">A STATE-OF-THE-ART CO-WORKING SPACE:</div>
  <div class="dots" style="left:360px;right:30px;top:252px"></div>
  <ul class="abs features">
    <li>LIGHT-FILLED common work space</li>
    <li>Private offices</li>
    <li>Conference room</li>
    <li>A riverfront balcony with stunning views</li>
  </ul>

  <p class="abs pitch">Work in an environment that <em>promotes creativity,</em><br><em>productivity, prosperity, and community.</em> A space<br>where you can learn, grow and connect with<br><em>open-minded, open-hearted people.</em></p>

  <div class="dots" style="left:420px;right:30px;top:438px;border-top-color:#bbb"></div>

  <div class="abs contact-line" style="top:448px">
    <span class="web">www.<b>keystonecommons</b>.com</span>
    <svg class="icon" viewBox="0 0 20 20"><circle cx="10" cy="10" r="9" fill="none" stroke="#333" stroke-width="1.2"/><circle cx="10" cy="10" r="5.5" fill="none" stroke="var(--orange)" stroke-width="1"/><path d="M4.5 10h11M10 4.5v11M6 7h8M6 13h8" stroke="var(--orange)" stroke-width=".8"/></svg>
  </div>
  <div class="abs contact-line" style="top:470px">
    <span class="addr">12 Ferry Ln., #8 Mill Building Riverton, NY</span>
    <svg class="icon" viewBox="0 0 20 20"><circle cx="10" cy="10" r="9" fill="none" stroke="#333" stroke-width="1.2"/><path d="M10 15.5c-3-3.6-4-5.5-4-7a4 4 0 0 1 8 0c0 1.5-1 3.4-4 7z" fill="var(--orange)"/><circle cx="10" cy="8.4" r="1.4" fill="#fff"/></svg>
  </div>
</section>

<!-- BACK: events and mailing side -->
<section class="card card--back" aria-label="Postcard back">
  <svg class="art" width="708" height="517" viewBox="0 0 708 517">
    <defs>
      <linearGradient id="panel" x1="0" y1="0" x2="1" y2="1">
        <stop offset="0" stop-color="#6a6a6a"/>
        <stop offset="1" stop-color="#585858"/>
      </linearGradient>
      <linearGradient id="talk" x1="0" y1="0" x2="1" y2="1">
        <stop offset="0" stop-color="#7a4a3a"/>
        <stop offset=".6" stop-color="#8e8a98"/>
        <stop offset="1" stop-color="#3e4f74"/>
      </linearGradient>
    </defs>
    <path d="M0,126 L300,126 C362,200 384,330 352,420 C322,482 262,517 214,517 L0,517 Z" fill="url(#panel)"/>
    <path d="M208,0 C320,70 362,160 352,260 C342,380 280,470 208,517" fill="none" stroke="var(--orange)" stroke-width="1.2"/>
    <circle role="img" aria-label="Photo of an audience at a talk in the event hall" cx="286" cy="139" r="56" fill="url(#talk)"/>
    <circle cx="286" cy="139" r="64" fill="none" stroke="var(--orange)" stroke-width="1.2"/>
  </svg>

  <span class="abs brand__dot" style="left:24px;top:34px;width:42px;height:42px"></span>
  <div class="brand" style="left:22px;top:88px;font-size:18px">the keystone commons</div>

  <div class="abs inst-title">THE KEYSTONE INSTITUTE</div>
  <div class="dots" style="left:21px;width:192px;top:154px"></div>
  <p class="abs inst-copy">Discover what it means to live a life aligned, as you explore the four dimensions of wealth. Join us for an inspiring array of classes, talks and workshops.</p>

  <div class="abs events-title">SOME OF OUR UPCOMING EVENTS INCLUDE:</div>
  <div class="dots" style="left:20px;width:320px;top:242px"></div>
  <div class="dots" style="left:20px;width:320px;top:294px"></div>
  <div class="dots" style="left:20px;width:330px;top:357px"></div>
  <div class="dots" style="left:20px;width:300px;top:405px"></div>
  <div class="abs" style="left:153px;top:243px;height:162px;border-left:1.5px dotted #ddd"></div>

  <div class="event" style="left:21px;top:246px">
    <div class="event__name">Wake Up Wall Street</div>
    <div class="event__host">with Owen Hartley and Sam Drucker</div>
    <div class="event__when">Thursday, March 15, 6 pm</div>
  </div>
  <div class="event" style="left:160px;top:246px">
    <div class="event__name">Experiential Philosophy Series</div>
    <div class="event__host">with Paul Montero</div>
    <div class="event__when">Mondays: March 19 &amp; April 16, 7 pm</div>
  </div>
  <div class="event" style="left:21px;top:298px">
    <div class="event__name">Literary Salon and<br>Book Signing</div>
    <div class="event__host">3-time Emmy winner, Nora Ellison</div>
    <div class="event__when">Thursday, March 22, 7 pm</div>
  </div>
  <div class="event" style="left:160px;top:298px">
    <div class="event__name">Psychotherapy &amp; Kabbalah</div>
    <div class="event__host">Dana Whitcombe &amp; Rabbi Eli Marsh</div>
    <div class="event__when">Wednesdays, March 28 &amp;<br>April 25, 6:30 pm</div>
  </div>
  <div class="event" style="left:21px;top:361px">
    <div class="event__name">Four Dimensions of Wealth</div>
    <div class="event__host">with Owner Sam Drucker</div>
    <div class="event__when">Thursday, April 12, 7 pm</div>
  </div>
  <div class="event" style="left:160px;top:361px">
    <div class="event__when" style="margin-top:0;line-height:1.5">Visit our website for information on<br>weekly meditation and yoga classes,<br>and more events.</div>
  </div>

  <div class="abs back-contact" style="top:413px;font-size:13px">
    <svg class="icon" viewBox="0 0 20 20"><circle cx="10" cy="10" r="9" fill="none" stroke="#fff" stroke-width="1.2"/><circle cx="10" cy="10" r="5.5" fill="none" stroke="var(--orange)" stroke-width="1"/><path d="M4.5 10h11M10 4.5v11M6 7h8M6 13h8" stroke="var(--orange)" stroke-width=".8"/></svg>
    <span>www.<b style="color:var(--orange);font-family:'Exo 2',sans-serif">keystonecommons</b>.com/events</span>
  </div>
  <div class="abs back-contact" style="top:438px;font-size:16px;letter-spacing:1px">
    <svg class="icon" viewBox="0 0 20 20"><circle cx="10" cy="10" r="9" fill="none" stroke="#fff" stroke-width="1.2"/><path d="M7 5.5l2 2.5-1.2 1.3c.7 1.4 1.6 2.3 2.9 2.9l1.3-1.2 2.5 2-1.2 1.6c-3.4-.4-6.8-3.8-7.2-7.2z" fill="var(--orange)"/></svg>
    <span>914.555.0142</span>
  </div>
  <div class="abs back-contact" style="top:461px;font-family:'Oswald',sans-serif;font-weight:500;font-size:10px">
    <svg class="icon" viewBox="0 0 20 20"><circle cx="10" cy="10" r="9" fill="none" stroke="#fff" stroke-width="1.2"/><path d="M10 15.5c-3-3.6-4-5.5-4-7a4 4 0 0 1 8 0c0 1.5-1 3.4-4 7z" fill="var(--orange)"/><circle cx="10" cy="8.4" r="1.4" fill="#fff"/></svg>
    <span>12 Ferry Ln., #8 Mill Building Riverton, NY</span>
  </div>

  <div class="abs postage">PRSRT STD<br>ECRWSS<br>U.S. Postage<br><b>PAID</b><br>LRC RETAIL</div>

  <div class="abs mailbox">
    <span class="mailbox__route">****************ECRWSS****</span>
    <span class="mailbox__to">Local<br>Postal Customer</span>
  </div>
</section>

</body>
</html>
```